Business Card Design

Cedar Gate Rentals
Cedar Gate Rentals is a high end home rental leasing company that provides exquisite properties in niche markets. We are a small family owned business that considers our clients not as renters, but as friends. Every property we buy must be brought up to our high standards before it is offered on the market. The properties that we lease are exceptional, "move in" ready homes. This allows for the client to take pride in their lease as if it was their own home. To put it another way; we do not lease a property that we would not live in ourselves.

Target Market(s)

Couples making $100K or more

Industry/Entity Type

Business

Requirements
Must have
• Some sort of logo
Nice to have
• good slogan
Should not have
• Pink

```html
<!DOCTYPE html>
<html lang="en">
<head>
<meta charset="utf-8">
<title>Cedar Gate Rentals – Business Card</title>
<link rel="stylesheet" href="https://fonts.googleapis.com/css2?family=Arvo:wght@700&family=Patrick+Hand&family=Open+Sans:wght@400&display=swap">
<style>
  :root {
    --page: #ffffff;
    --wood-light: #8a3a1c;
    --wood-mid: #5a2210;
    --wood-dark: #2a0e05;
    --title: #f6f1ea;
    --slogan: #f4e01c;
    --contact: #ffffff;
    --web: #c9953c;
  }
  * { margin: 0; padding: 0; box-sizing: border-box; }
  html, body {
    width: 1200px;
    height: 702px;
    overflow: hidden;
    background: var(--page);
  }
  .card {
    position: absolute;
    left: 44px;
    top: 44px;
    width: 1109px;
    height: 614px;
    overflow: hidden;
  }
  .card__wood {
    position: absolute;
    inset: 0;
    background:
      radial-gradient(ellipse 60% 70% at 50% 52%, var(--wood-light) 0%, var(--wood-mid) 55%, var(--wood-dark) 100%);
  }
  .card__text {
    position: absolute;
    left: 0;
    width: 100%;
    text-align: center;
    white-space: nowrap;
  }
  .brand-name {
    top: 160px;
    font-family: "Arvo", serif;
    font-weight: 700;
    font-size: 76px;
    letter-spacing: 1px;
    color: var(--title);
    padding-left: 12px;
  }
  .slogan {
    position: absolute;
    right: 50px;
    top: 246px;
    font-family: "Patrick Hand", cursive;
    font-size: 46px;
    letter-spacing: 2px;
    color: var(--slogan);
    white-space: nowrap;
  }
  .person-name {
    top: 322px;
    font-family: "Open Sans", sans-serif;
    font-size: 44px;
    color: var(--contact);
    padding-left: 22px;
  }
  .phone {
    top: 384px;
    font-family: "Open Sans", sans-serif;
    font-size: 48px;
    color: var(--contact);
    padding-left: 22px;
  }
  .web-line {
    font-family: "Open Sans", sans-serif;
    font-size: 23px;
    color: var(--web);
    padding-left: 22px;
  }
  .website { top: 491px; }
  .email { top: 530px; }
</style>
</head>
<body>
  <main class="card">
    <div class="card__wood" role="img" aria-label="Dark polished hardwood floor planks background with a warm glow in the centre"></div>
    <h1 class="card__text brand-name">Cedar Gate Rentals</h1>
    <p class="slogan">welcome home!</p>
    <p class="card__text person-name">Jane Doe</p>
    <p class="card__text phone">123 456 7890</p>
    <p class="card__text web-line website">www.cedargaterentals.com</p>
    <p class="card__text web-line email">sales@cedargaterentals.com</p>
  </main>
</body>
</html>
```